Soltravex business card

a nice business card with the logo,
Soltravex
Delia Vostrand
Marketing Director
CH-1296 Geneva
Switzerland
+41 79 612 3048
email: Delia.Vostrand@soltravex-mail.net

Target Market(s)

fertilizer business people, very nice and classic business card, normal size, make it nice and funky, try to make it different from the normal boring ones if possible.

Industry/Entity Type

Farming

Number of Pages Required

1 page

Requirements
Must have
• logo, Soltravex, my name - mail and phone number
regular business card size for me to print easy please

```html
<!DOCTYPE html>
<html lang="en">
<head>
<meta charset="utf-8">
<title>Soltravex business card</title>
<link rel="stylesheet" href="https://fonts.googleapis.com/css2?family=Barlow:wght@600&family=Share+Tech&display=swap">
<style>
  :root {
    --card-yellow: #fbf800;
    --leaf-green: #9eff0a;
    --brand-grey: #a3a79a;
    --name-red: #f50f0f;
    --ink: #111111;
    --page: #ffffff;
  }
  * { margin: 0; padding: 0; box-sizing: border-box; }
  html, body {
    width: 989px;
    height: 1200px;
    overflow: hidden;
    background: var(--page);
  }
  .sheet {
    position: relative;
    width: 989px;
    height: 1200px;
  }
  .card {
    position: absolute;
    left: 3px;
    width: 985px;
    height: 563px;
    background: var(--card-yellow);
    border-radius: 37px;
    overflow: hidden;
  }
  .card--front { top: 0; }
  .card--back { top: 636px; }

  .brand-dot {
    position: absolute;
    left: 428px;
    top: 180px;
    width: 120px;
    height: 120px;
    border-radius: 50%;
    background: var(--leaf-green);
  }
  .brand-name {
    position: absolute;
    font-family: "Barlow", "Arial", sans-serif;
    font-weight: 600;
    color: var(--brand-grey);
    text-transform: uppercase;
    white-space: nowrap;
    line-height: 1;
  }
  .card--front .brand-name {
    left: 0;
    width: 985px;
    top: 435px;
    text-align: center;
    font-size: 25px;
    letter-spacing: 17px;
    padding-left: 17px;
  }
  .card--back .brand-name {
    left: 253px;
    top: 44px;
    font-size: 46px;
    letter-spacing: 26px;
  }

  .green-bands {
    position: absolute;
    left: 0;
    top: 0;
    width: 985px;
    height: 563px;
  }
  .green-bands polygon { fill: var(--leaf-green); }

  .holder {
    position: absolute;
    left: 253px;
    top: 98px;
    font-family: "Share Tech", "Arial Narrow", sans-serif;
    white-space: nowrap;
    line-height: 1;
  }
  .holder__name {
    color: var(--name-red);
    font-size: 26px;
    letter-spacing: 0.5px;
  }
  .holder__role {
    color: var(--ink);
    font-size: 19px;
    letter-spacing: 0.5px;
  }

  .contact {
    position: absolute;
    font-family: "Share Tech", "Arial Narrow", sans-serif;
    font-size: 21px;
    color: var(--ink);
    white-space: nowrap;
    line-height: 1;
    display: flex;
    align-items: center;
    gap: 10px;
  }
  .contact--phone { top: 425px; right: 458px; letter-spacing: 2.6px; }
  .contact--address { top: 466px; right: 473px; letter-spacing: 3px; }
  .contact--email { top: 507px; right: 480px; letter-spacing: 1.4px; }
  .contact__icon { width: 31px; height: 19px; }
</style>
</head>
<body>
<main class="sheet">
  <section class="card card--front" aria-label="Card front">
    <div class="brand-dot"></div>
    <p class="brand-name">Soltravex</p>
  </section>

  <section class="card card--back" aria-label="Card back">
    <svg class="green-bands" viewBox="0 0 985 563" aria-hidden="true">
      <polygon points="788,0 837,0 635,563 527,563"/>
      <polygon points="955,0 975,0 855,563 700,563"/>
      <polygon points="985,460 985,563 928,563"/>
    </svg>
    <p class="brand-name">Soltravex</p>
    <p class="holder">
      <span class="holder__name">Delia Vostrand</span>
      <span class="holder__role">/ Marketing Director</span>
    </p>
    <p class="contact contact--phone">+41 79 612 3048</p>
    <p class="contact contact--address">CH-1296 Geneva, Switzerland</p>
    <p class="contact contact--email">
      <svg class="contact__icon" viewBox="0 0 31 19" aria-hidden="true">
        <rect x="0.75" y="0.75" width="29.5" height="17.5" fill="none" stroke="#111" stroke-width="1.5"/>
        <polyline points="0.75,0.75 15.5,11 30.25,0.75" fill="none" stroke="#111" stroke-width="1.5"/>
      </svg>
      Delia.Vostrand@soltravex-mail.net
    </p>
  </section>
</main>
</body>
</html>
```